Granite Ridge College-Pinecrest Welcome Week

I am the Student Activities Coordinator at Granite Ridge College-Pinecrest. For Welcome Week 2013, I need a standard poster 24x36 with the list of events happening. Our theme is based on the popular Friday Late Laughs video "We Got a Kite"
http://www.vidtrove.example/clip/Q4mZp8sLwTe
Our theme is:
We're at the 'Crest!
Welcome Week 2013
Graphics on the poster should reflect popular images/designs of FLL We Got a Kite. However, the boat should be a steamboat instead of the yacht image.
Unfortunately, I have a lot of text to fit on the poster. Traditionally we go with 3 margins listing events. I'm attaching the word document of events and our logo to this proposal. I'll also attach a few google images of "We Got a Kite" that align with the type of theme I'm looking for.
One last thing, our logo contains mountains listing all of the different campuses. Remove the campus names and mountains all together. Use simply the Colorado flag C and "Granite Ridge College".
Thanks for considering this brief!
Glen
Target Market(s)
Our college students love to ski and snowboard. In fact, one of our degrees is "Alpine Slope Commerce". Their ages are 18-22.
Industry/Entity Type
Events
Look and feel

```html
<!DOCTYPE html>
<html lang="en">
<head>
<meta charset="utf-8">
<title>Granite Ridge College Welcome Week 2013</title>
<link rel="stylesheet" href="https://fonts.googleapis.com/css2?family=Ubuntu:wght@700&family=PT+Sans+Narrow:wght@400;700&display=swap">
<style>
:root{
  --backdrop:#d9d9db;
  --paper:#ffffff;
  --sky:#bfe0f3;
  --sky-deep:#5aaee0;
  --ocean:#1f74b8;
  --navy:#1d3f78;
  --heading:#3b4794;
  --event:#3d55a8;
  --ink:#3c3c3c;
  --orange:#f08a1e;
  --red-orange:#d9481c;
}
*{margin:0;padding:0;box-sizing:border-box}
html,body{width:1200px;height:900px;overflow:hidden;background:var(--backdrop)}
.poster{
  position:absolute;left:320px;top:30px;width:560px;height:840px;
  background:
    radial-gradient(ellipse 260px 160px at 90px 70px,rgba(90,174,224,.45),transparent 70%),
    radial-gradient(ellipse 220px 120px at 420px 40px,rgba(191,224,243,.7),transparent 70%),
    radial-gradient(ellipse 300px 200px at 120px 600px,rgba(90,174,224,.55),transparent 70%),
    var(--paper);
  box-shadow:0 6px 18px rgba(0,0,0,.25);
  overflow:hidden;
  font-family:"PT Sans Narrow",sans-serif;
}
.college-mark{position:absolute;left:26px;top:30px;display:flex;align-items:center;gap:5px}
.college-mark .dot{width:18px;height:18px;border-radius:50%;background:var(--navy)}
.college-mark .name{font-weight:700;font-size:11px;line-height:1;color:var(--navy);width:70px;text-transform:uppercase}
.theme{position:absolute;left:50px;top:60px;width:330px;height:280px}
.theme-art{position:absolute;inset:0;border-radius:165px 165px 30px 30px;
  background:linear-gradient(180deg,rgba(191,224,243,.55) 0%,rgba(255,255,255,.3) 45%,rgba(90,174,224,.55) 70%,rgba(29,79,134,.85) 100%)}
.theme-title{position:absolute;left:0;width:100%;text-align:center;font-family:"Ubuntu",sans-serif;font-weight:700;letter-spacing:-1px;line-height:1}
.theme-title.top{top:88px;font-size:44px;color:var(--ocean)}
.theme-title.bottom{top:138px;font-size:58px;
  background:linear-gradient(180deg,var(--orange),var(--red-orange));-webkit-background-clip:text;background-clip:text;-webkit-text-fill-color:transparent}
.theme-sub{position:absolute;left:0;width:100%;top:212px;font-family:"Ubuntu",sans-serif;font-weight:700;font-size:14px;line-height:1.05;color:#fff;text-align:center}
.boat-photo{position:absolute;left:20px;top:350px;width:290px;height:190px;
  background:linear-gradient(180deg,rgba(255,255,255,0) 0%,#e9eef2 35%,#ffffff 60%,#9fcbe8 85%,#5aaee0 100%);border-radius:4px}
.free-note{position:absolute;left:50px;top:590px;text-align:center;color:var(--navy);font-family:"Ubuntu",sans-serif;font-weight:700;line-height:1}
.free-note .small{font-size:10px}
.free-note .big{font-size:30px;letter-spacing:1px}
.schedule-col{position:absolute;font-size:8.6px;line-height:1.13;color:var(--ink)}
.col-one{left:190px;top:600px;width:130px}
.col-two{left:325px;top:370px;width:118px}
.col-three{left:443px;top:252px;width:112px}
.day{margin-bottom:5px;padding-top:3px;border-top:1px solid var(--sky-deep)}
.day:first-child{border-top:none}
.day-title{font-weight:700;color:var(--heading);font-size:9px}
.event{padding-left:8px}
.event-name{font-weight:700;color:var(--event);margin-left:-4px}
.bands{position:absolute;left:0;bottom:0;width:100%;height:60px}
</style>
</head>
<body>
<main class="poster">
  <div class="college-mark"><span class="dot"></span><span class="name">Granite Ridge College</span></div>

  <section class="theme">
    <div class="theme-art" role="img" aria-label="Theme emblem artwork: sweeping blue arc, birds and sail over wave ribbon"></div>
    <div class="theme-title top">WE GOT A</div>
    <div class="theme-title bottom">KITE</div>
    <div class="theme-sub">WELCOME<br>WEEK 2013</div>
  </section>

  <div class="boat-photo" role="img" aria-label="Photo of a white boat cruising on blue water"></div>

  <div class="free-note">
    <div class="small">ALL EVENTS ARE</div>
    <div class="big">FREE</div>
    <div class="small">UNLESS OTHERWISE NOTED</div>
  </div>

  <section class="schedule-col col-one">
    <div class="day">
      <div class="day-title">Thursday August 22:</div>
      <div class="event">Residence Hall Move-In<br>12:00pm-3:00pm<br>Hill Hall</div>
      <div class="event"><div class="event-name">Brunch</div>10:00am-1:00pm<br>Dining Hall</div>
      <div class="event"><div class="event-name">International<br>Students Orientation</div>3:00pm<br>Ridgeview 121</div>
      <div class="event"><div class="event-name">Dinner</div>5:00pm-6:30pm<br>Dining Hall<br>Hot Springs Waterslide Party<br>7:00pm-9:00pm<br>Riverside Hot Springs</div>
    </div>
  </section>

  <section class="schedule-col col-two">
    <div class="day">
      <div class="day-title">Friday August 23:</div>
      <div class="event"><div class="event-name">Breakfast</div>7:30am-9:00am<br>Dining Hall</div>
      <div class="event"><div class="event-name">Hike Cedar Run Falls</div>9:00am-11:30am<br>Shuttle leaves Hill Hall at 8:30am</div>
      <div class="event"><div class="event-name">BBQ and Faculty Ice Cream Social</div>12:00pm-1:30pm<br>Dining Hall</div>
      <div class="event"><div class="event-name">Kick Off Party: Inflatables</div>1:30pm-4:00pm<br>Upper Parking Lot</div>
      <div class="event"><div class="event-name">Dinner</div>5:00pm-6:00pm<br>Dining Hall</div>
      <div class="event"><div class="event-name">Free Concert</div>7:00pm<br>Pinecrest Resort Base<br>(PRT Buses to Resort,<br>5:35pm Last Bus)</div>
    </div>
    <div class="day">
      <div class="day-title">Saturday August 24:</div>
      <div class="event">Main Street Farmers Market<br>9:00am-2:00pm<br>6th &amp; Spruce (walking dist.)</div>
      <div class="event"><div class="event-name">Brunch</div>10:00am-1:00pm<br>Dining Hall</div>
      <div class="event"><div class="event-name">Juniper Park Hot Springs</div>2:00pm-5:00pm<br>Shuttle leaves Hill Hall at 1:30pm</div>
      <div class="event"><div class="event-name">Dinner</div>5:00-6:00pm<br>Dining Hall</div>
      <div class="event"><div class="event-name">Free Movie on the Mountain:</div>Summit Quest 8:00pm<br>(PRT Buses to Resort, 5:35pm<br>Last Bus)</div>
    </div>
  </section>

  <section class="schedule-col col-three">
    <div class="day">
      <div class="day-title">Sunday August 25:</div>
      <div class="event"><div class="event-name">Brunch</div>10:00am-1:00pm<br>Dining Hall</div>
      <div class="event"><div class="event-name">Alpine Slide/Volleyball</div>2:00pm-4:00pm<br>Meet at Larkspur Hill</div>
      <div class="event"><div class="event-name">Dinner</div>5:00pm-6:00pm<br>Dining Hall</div>
      <div class="event"><div class="event-name">Mandatory All<br>Hall Meeting</div>6:00pm<br>Auditorium</div>
      <div class="event"><div class="event-name">RHA Super Sunday<br>Program</div>8:00pm<br>Hill Hall: MPR</div>
    </div>
    <div class="day">
      <div class="day-title">Monday August 26:</div>
      <div class="event">Regular Dining Hall Hours Begin</div>
      <div class="event"><div class="event-name">“Being Alone Sucks!”</div>9:00pm<br>Auditorium</div>
    </div>
    <div class="day">
      <div class="day-title">Tuesday August 27:</div>
      <div class="event"><div class="event-name">Newly Roommate Game</div>7:00pm-8:00pm<br>Hill Hall: MPR</div>
      <div class="event"><div class="event-name">Free Gelato</div>8:00pm-9:00pm<br>Dolce Scoop 7th and Willow</div>
    </div>
    <div class="day">
      <div class="day-title">Wednesday August 28:</div>
      <div class="event"><div class="event-name">Free Bowling</div>9:00pm<br>Frost Lanes</div>
    </div>
    <div class="day">
      <div class="day-title">Thursday August 29:</div>
      <div class="event"><div class="event-name">Club Fair</div>10:00am-2:00pm<br>Dining Hall</div>
      <div class="event"><div class="event-name">Black Light Dodgeball</div>9:00pm<br>Gym</div>
    </div>
    <div class="day">
      <div class="day-title">Friday August 30:</div>
      <div class="event"><div class="event-name">Late Night Climbing</div>9:00pm<br>Gym</div>
    </div>
  </section>

  <svg class="bands" viewBox="0 0 560 60" width="560" height="60" preserveAspectRatio="none" aria-hidden="true">
    <path d="M0 34 L560 14 L560 24 L0 44 Z" fill="#2d5f9a"/>
    <path d="M0 47 L560 27 L560 29 L0 49 Z" fill="#5aaee0"/>
    <path d="M0 52 L560 32 L560 60 L0 60 Z" fill="#1d3f78"/>
  </svg>
</main>
</body>
</html>
```